DEAN COLLOPY PROPERTY SERVICES

I want a business card that is clean and simple.
'Dean Collopy Property Services' is the title.
Somewhere on the card needs to be 'Carpentry, Tiling, painting and garden services'

On the back of card
PH 087 394 1526
email: deancollopypropertyservices@bluefinchmail.net

I have attached a picture of my other business. I would like the font and design to be similar to the bathroom business.

Many thanks.

```html
<!DOCTYPE html>
<html lang="en">
<head>
<meta charset="utf-8">
<title>Dean Collopy Property Services – Business Card</title>
<link href="https://fonts.googleapis.com/css2?family=Montserrat:wght@400;500;600;700&display=swap" rel="stylesheet">
<style>
  :root {
    --backdrop: #5c5c5c;
    --backdrop-dark: #3e3e3e;
    --ink: #141414;
    --card-black: #121212;
    --card-white: #f4f4f4;
    --card-white-shade: #dcdcdc;
    --text-light: #ffffff;
    --text-muted: #b9b9b9;
    --accent-cream: #ece6c8;
  }
  * { margin: 0; padding: 0; box-sizing: border-box; }
  html, body { width: 1200px; height: 900px; overflow: hidden; }
  body {
    position: relative;
    font-family: "Montserrat", sans-serif;
    background: radial-gradient(ellipse at 50% 40%, var(--backdrop) 0%, var(--backdrop-dark) 100%);
  }
  .card {
    position: absolute;
    width: 680px;
    height: 390px;
    border-radius: 26px;
    overflow: hidden;
    box-shadow: 0 18px 40px rgba(0,0,0,0.45);
  }

  /* Front */
  .card-front {
    left: 60px; top: 50px;
    background: linear-gradient(160deg, var(--card-white) 0%, #ffffff 45%, var(--card-white-shade) 100%);
  }
  .wordmark {
    position: absolute;
    left: 0; right: 0;
    text-align: center;
    font-weight: 600;
    line-height: 1;
  }
  .wordmark-name { font-size: 64px; letter-spacing: 1px; }
  .wordmark-tag { font-size: 22px; letter-spacing: 7px; margin-top: 14px; }
  .card-front .wordmark { top: 88px; color: var(--ink); }

  .services-band {
    position: absolute;
    left: 0; right: 0; bottom: 0;
    height: 112px;
    background: var(--card-black);
  }
  .services-rule {
    position: absolute;
    left: 0; right: 0; top: 6px;
    height: 2px;
    background: var(--card-white);
  }
  .services-label {
    position: absolute;
    left: 50%; top: -8px;
    transform: translateX(-50%);
    padding: 5px 16px;
    border: 2px solid var(--card-white);
    border-radius: 20px;
    background: var(--card-black);
    color: var(--text-light);
    font-size: 15px;
    font-weight: 500;
    letter-spacing: 1px;
  }
  .services-list {
    position: absolute;
    left: 40px; right: 40px; top: 54px;
    display: flex;
    justify-content: space-between;
    list-style: none;
    color: var(--text-light);
    font-size: 19px;
    font-weight: 600;
  }
  .services-list li::before {
    content: "";
    display: inline-block;
    width: 7px; height: 7px;
    border-radius: 50%;
    background: var(--text-light);
    margin-right: 12px;
    vertical-align: middle;
  }

  /* Back */
  .card-back {
    left: 460px; top: 470px;
    background: linear-gradient(160deg, #1c1c1c 0%, var(--card-black) 60%, #0a0a0a 100%);
  }
  .card-back .wordmark { top: 92px; color: var(--text-light); }
  .contact-block {
    position: absolute;
    left: 0; right: 0; top: 272px;
    display: flex;
    justify-content: center;
    align-items: center;
    gap: 22px;
  }
  .person { text-align: right; }
  .person-name { color: var(--accent-cream); font-size: 24px; font-weight: 700; }
  .person-role { color: var(--text-muted); font-size: 14px; margin-top: 4px; }
  .divider { width: 2px; height: 58px; background: var(--text-light); }
  .contact-lines { list-style: none; color: var(--text-muted); font-size: 14px; }
  .contact-lines li { display: flex; align-items: center; gap: 12px; line-height: 28px; }
  .contact-lines svg { width: 16px; height: 16px; fill: var(--text-light); }
</style>
</head>
<body>

<section class="card card-front" aria-label="Card front">
  <div class="wordmark">
    <div class="wordmark-name">Dean Collopy</div>
    <div class="wordmark-tag">PROPERTY SERVICES</div>
  </div>
  <div class="services-band">
    <div class="services-rule"></div>
    <div class="services-label">SERVICES</div>
    <ul class="services-list">
      <li>Carpentry</li>
      <li>Tiling</li>
      <li>Painting</li>
      <li>Garden Services</li>
    </ul>
  </div>
</section>

<section class="card card-back" aria-label="Card back">
  <div class="wordmark">
    <div class="wordmark-name">Dean Collopy</div>
    <div class="wordmark-tag">PROPERTY SERVICES</div>
  </div>
  <div class="contact-block">
    <div class="person">
      <div class="person-name">Dean Collopy</div>
      <div class="person-role">Realtor</div>
    </div>
    <div class="divider"></div>
    <ul class="contact-lines">
      <li>
        <svg viewBox="0 0 24 24" aria-hidden="true"><path d="M6.6 10.8a15.1 15.1 0 0 0 6.6 6.6l2.2-2.2a1 1 0 0 1 1-.25 11.4 11.4 0 0 0 3.6.57 1 1 0 0 1 1 1V20a1 1 0 0 1-1 1A17 17 0 0 1 3 4a1 1 0 0 1 1-1h3.5a1 1 0 0 1 1 1c0 1.25.2 2.45.57 3.57a1 1 0 0 1-.25 1z"/></svg>
        087 394 1526
      </li>
      <li>
        <svg viewBox="0 0 24 24" aria-hidden="true"><path d="M2 5h20v14H2z M3.5 6.5 12 13l8.5-6.5" fill="none" stroke="#fff" stroke-width="2"/></svg>
        deancollopypropertyservices@bluefinchmail.net
      </li>
    </ul>
  </div>
</section>

</body>
</html>
```